Create a Professional PowerPoint Slide Deck

I need a professional looking and editable PowerPoint presentation with contents based on the attached PDF.

I would like to see the following;
- add design elements to every slide (cover, title, contents etc)
- enhance the graphs or charts
- same copy will be used
I'm attaching the document to be put into powerpoint (KWRO white paper: "Cargo Wise")

Target Market(s)

Executives and managers responsible for the distribution of products

Industry/Entity Type

It Professional

Font styles to use
Serif

Colors

Designer to choose colors to be used in the design.

Requirements
Must have
• The format should be portrait orientation as this may be printed on paper and converted to PDF for distribution
• Complete conversion of all pages in the attached White Paper
• Upgraded graphics and formatting
Nice to have
• Any creative ideas to make the presentation more attractive or easier to understand
• Color scheme should complement the KWRO Freightlines Logo (red and black)

```html
<!DOCTYPE html>
<html lang="en">
<head>
<meta charset="utf-8">
<title>Use Your Data to Improve Logistics – KWRO Freightlines</title>
<link href="https://fonts.googleapis.com/css2?family=Arimo:wght@400;700&display=swap" rel="stylesheet">
<style>
  :root{
    --red:#e3101f;
    --ink:#3a3a3a;
    --grey:#9a9a9a;
    --rule:#d6d6d6;
    --panel:#f1f1f1;
    --bg:#e4e4e4;
    --paper:#ffffff;
    --token:#b3b3b3;
  }
  *{box-sizing:border-box;margin:0;padding:0}
  html,body{width:1200px;height:800px;overflow:hidden}
  body{background:var(--bg);font-family:"Arimo",Arial,sans-serif;color:var(--ink);position:relative}
  .page{position:absolute;background:var(--paper)}
  .page-left{left:57px;top:64px;width:504px;height:672px}
  .page-right{left:634px;top:64px;width:508px;height:678px}
  .abs{position:absolute}
  .page-title{left:37px;top:30px;font-size:11.4px;font-weight:700;line-height:13px}
  .page-title .lead{color:var(--red);display:block}
  .page-title .sub{color:#b0b0b0;display:block}
  .title-rule{left:37px;top:62px;width:237px;height:3px;background:#dcdcdc}
  .brand{top:26px;display:flex;align-items:center;gap:6px;font-size:24px;font-weight:700;color:var(--red);letter-spacing:1px}
  .brand .dot{width:20px;height:20px;border-radius:50%;border:2px solid var(--red)}
  .page-left .brand{left:356px}
  .page-right .brand{left:360px}
  .body-text{font-size:9.6px;line-height:11.2px;color:#444;text-align:justify}
  .body-text.ragged{text-align:left}
  .thumb{background:#fff;border:1px solid #dedede}
  .caption{background:var(--panel);border-top:1px solid var(--red);padding:6px 6px;line-height:12px}
  .caption .fig{color:var(--red);font-size:10px;font-weight:700;display:block;line-height:12px}
  .caption .note{display:block;color:#8a8a8a;font-size:7.4px;font-weight:700;line-height:9px;margin-top:1px}
  .footer-rule{height:1px;background:var(--rule)}
  .page-num{font-size:7.5px;color:#888}
  .section-head{color:var(--red);font-size:14.5px;font-weight:700}
  .diagram{left:186px;top:110px;width:322px;height:272px;background:var(--panel)}
  .map-fill{background:linear-gradient(135deg,#c9dcea,#e4ece0)}
</style>
</head>
<body>

<!-- Page 05 -->
<section class="page page-left">
  <h1 class="abs page-title"><span class="lead">USE YOUR DATA TO IMPROVE LOGISTICS</span><span class="sub">PROCESSES AND PROFITS</span></h1>
  <div class="abs title-rule"></div>
  <div class="abs brand"><span class="dot"></span>KWRO</div>

  <p class="abs body-text" style="left:34px;top:114px;width:438px">KWRO takes your data and processes it through software that produces reports which yield important insights to your logistics program. These reports are reduced to Key Performance Indicators (KPI’s) which are published monthly and reviewed with management to spot trends early and make necessary adjustments to your processes (Fig. 4). These reports are provided at no cost as long as you are shipping with one of KWRO’s partners. If you would like to have other data included which has not been captured by the TMS, this can be done for a fee.</p>

  <div class="abs thumb" style="left:34px;top:198px;width:138px;height:180px">
    <svg width="138" height="180" viewBox="0 0 138 180">
      <text x="5" y="12" font-size="6.2" font-weight="700" fill="#222">Brightline Goods: Supply Chain KPI's</text>
      <text x="5" y="21" font-size="4" fill="#333">LTL Summary</text>
      <g stroke="#9aa" stroke-width=".5">
        <line x1="5" y1="23" x2="95" y2="23"/>
        <line x1="5" y1="27" x2="95" y2="27"/><line x1="5" y1="31" x2="95" y2="31"/><line x1="5" y1="35" x2="95" y2="35"/><line x1="5" y1="39" x2="95" y2="39"/><line x1="5" y1="43" x2="95" y2="43"/><line x1="5" y1="47" x2="95" y2="47"/><line x1="5" y1="51" x2="95" y2="51"/>
      </g>
      <text x="5" y="63" font-size="4.4" fill="#333">Monthly Data</text>
      <g stroke="#9aa" stroke-width=".5">
        <rect x="5" y="66" width="128" height="6" fill="none"/>
        <line x1="5" y1="76" x2="133" y2="76"/><line x1="5" y1="80" x2="133" y2="80"/><line x1="5" y1="84" x2="133" y2="84"/><line x1="5" y1="88" x2="133" y2="88"/><line x1="5" y1="92" x2="133" y2="92"/><line x1="5" y1="96" x2="133" y2="96"/><line x1="5" y1="100" x2="133" y2="100"/><line x1="5" y1="104" x2="133" y2="104"/><line x1="5" y1="108" x2="133" y2="108"/><line x1="5" y1="112" x2="133" y2="112"/><line x1="5" y1="116" x2="133" y2="116"/><line x1="5" y1="120" x2="133" y2="120"/><line x1="5" y1="124" x2="133" y2="124"/><line x1="5" y1="128" x2="133" y2="128"/><line x1="5" y1="132" x2="133" y2="132"/><line x1="5" y1="136" x2="133" y2="136"/>
      </g>
    </svg>
  </div>
  <div class="abs thumb" style="left:181px;top:198px;width:141px;height:180px">
    <svg width="141" height="180" viewBox="0 0 141 180">
      <text x="5" y="12" font-size="4.6" fill="#333">12 Mo Moving Total</text>
      <g stroke="#9aa" stroke-width=".5">
        <rect x="5" y="15" width="131" height="5" fill="none"/>
        <line x1="5" y1="24" x2="136" y2="24"/><line x1="5" y1="28" x2="136" y2="28"/><line x1="5" y1="32" x2="136" y2="32"/><line x1="5" y1="36" x2="136" y2="36"/><line x1="5" y1="40" x2="136" y2="40"/><line x1="5" y1="44" x2="136" y2="44"/><line x1="5" y1="48" x2="136" y2="48"/>
      </g>
      <rect x="14" y="56" width="112" height="72" fill="#fff" stroke="#bbb" stroke-width=".6"/>
      <g stroke="#e2e2e2" stroke-width=".4">
        <line x1="20" y1="70" x2="122" y2="70"/><line x1="20" y1="84" x2="122" y2="84"/><line x1="20" y1="98" x2="122" y2="98"/><line x1="20" y1="112" x2="122" y2="112"/>
      </g>
      <polyline points="22,64 32,76 42,86 52,94 62,100 72,104 82,107 92,109 102,110 112,111 120,112" fill="none" stroke="#5b9bd5" stroke-width="1"/>
      <text x="34" y="146" font-size="3.6" fill="#888">Avg cost per shipment by month</text>
    </svg>
  </div>
  <div class="abs thumb" style="left:331px;top:198px;width:141px;height:180px">
    <svg width="141" height="180" viewBox="0 0 141 180">
      <text x="5" y="12" font-size="4.6" fill="#333">Top LTL Destinations, August, 2016</text>
      <g stroke="#9aa" stroke-width=".5">
        <line x1="5" y1="17" x2="85" y2="17"/><line x1="5" y1="21" x2="85" y2="21"/><line x1="5" y1="25" x2="85" y2="25"/><line x1="5" y1="29" x2="85" y2="29"/>
      </g>
    </svg>
    <div class="abs map-fill" role="img" aria-label="Map of the United States marking top shipment destinations" style="left:8px;top:44px;width:118px;height:62px"></div>
  </div>

  <div class="abs caption" style="left:34px;top:386px;width:438px;height:32px">
    <span class="fig">FIGURE 4.</span>
    <span class="note">Easy to read Dashboard reports provide previously unseen insights to your logistics system</span>
  </div>

  <p class="abs body-text ragged" style="left:34px;top:440px;width:126px">In addition to the Dashboard reports, other reports let you dig deeper to discover additional opportunities for improvement and cost savings (Fig 5). KWRO prepares and helps you interpret these reports so that you get maximum benefit from your data.</p>

  <div class="abs caption" style="left:34px;top:562px;width:124px;height:52px">
    <span class="fig">FIGURE 5.</span>
    <span class="note">Additional reports let you dig deeper for more sophisticated analysis</span>
  </div>

  <div class="abs thumb" style="left:186px;top:438px;width:136px;height:176px">
    <svg width="136" height="176" viewBox="0 0 136 176">
      <text x="6" y="9" font-size="4" fill="#333">Brightline Goods</text>
      <g font-size="3.4" fill="#333">
        <rect x="6" y="13" width="36" height="5" fill="none" stroke="#999" stroke-width=".4"/><text x="8" y="17">Origin 02720</text>
        <rect x="6" y="45" width="36" height="5" fill="none" stroke="#999" stroke-width=".4"/><text x="8" y="49">Origin 00048</text>
        <rect x="6" y="77" width="36" height="5" fill="none" stroke="#999" stroke-width=".4"/><text x="8" y="81">Origin 06085</text>
        <rect x="6" y="109" width="36" height="5" fill="none" stroke="#999" stroke-width=".4"/><text x="8" y="113">Origin 00701</text>
        <rect x="6" y="141" width="36" height="5" fill="none" stroke="#999" stroke-width=".4"/><text x="8" y="145">Origin 00872</text>
      </g>
      <g stroke="#bbb" stroke-width=".4">
        <line x1="6" y1="23" x2="130" y2="23"/><line x1="6" y1="28" x2="100" y2="28"/><line x1="6" y1="33" x2="100" y2="33"/><line x1="6" y1="38" x2="100" y2="38"/>
        <line x1="6" y1="55" x2="130" y2="55"/><line x1="6" y1="60" x2="100" y2="60"/><line x1="6" y1="65" x2="100" y2="65"/><line x1="6" y1="70" x2="100" y2="70"/>
        <line x1="6" y1="87" x2="130" y2="87"/><line x1="6" y1="92" x2="100" y2="92"/><line x1="6" y1="97" x2="100" y2="97"/>
        <line x1="6" y1="119" x2="130" y2="119"/><line x1="6" y1="124" x2="100" y2="124"/><line x1="6" y1="129" x2="100" y2="129"/>
        <line x1="6" y1="151" x2="130" y2="151"/><line x1="6" y1="156" x2="100" y2="156"/><line x1="6" y1="161" x2="100" y2="161"/>
      </g>
    </svg>
  </div>
  <div class="abs thumb" style="left:333px;top:438px;width:137px;height:176px">
    <svg width="137" height="176" viewBox="0 0 137 176">
      <text x="6" y="9" font-size="4" fill="#333">Brightline Goods</text>
      <g stroke="#bbb" stroke-width=".4">
        <line x1="6" y1="15" x2="130" y2="15"/><line x1="6" y1="20" x2="130" y2="20"/><line x1="6" y1="25" x2="100" y2="25"/><line x1="6" y1="30" x2="100" y2="30"/><line x1="6" y1="35" x2="100" y2="35"/><line x1="6" y1="40" x2="100" y2="40"/><line x1="6" y1="45" x2="100" y2="45"/><line x1="6" y1="50" x2="100" y2="50"/><line x1="6" y1="55" x2="100" y2="55"/><line x1="6" y1="60" x2="100" y2="60"/><line x1="6" y1="65" x2="100" y2="65"/><line x1="6" y1="70" x2="100" y2="70"/><line x1="6" y1="75" x2="100" y2="75"/><line x1="6" y1="80" x2="100" y2="80"/><line x1="6" y1="85" x2="100" y2="85"/><line x1="6" y1="90" x2="100" y2="90"/><line x1="6" y1="95" x2="100" y2="95"/><line x1="6" y1="100" x2="100" y2="100"/><line x1="6" y1="105" x2="100" y2="105"/><line x1="6" y1="110" x2="130" y2="110"/><line x1="6" y1="115" x2="100" y2="115"/><line x1="6" y1="120" x2="100" y2="120"/><line x1="6" y1="125" x2="100" y2="125"/><line x1="6" y1="130" x2="100" y2="130"/><line x1="6" y1="135" x2="100" y2="135"/><line x1="6" y1="140" x2="100" y2="140"/><line x1="6" y1="145" x2="100" y2="145"/><line x1="6" y1="150" x2="100" y2="150"/><line x1="6" y1="155" x2="100" y2="155"/>
      </g>
    </svg>
  </div>

  <div class="abs footer-rule" style="left:34px;top:638px;width:396px"></div>
  <span class="abs page-num" style="left:461px;top:634px">05</span>
</section>

<!-- Page 06 -->
<section class="page page-right">
  <h1 class="abs page-title"><span class="lead">USE YOUR DATA TO IMPROVE LOGISTICS</span><span class="sub">PROCESSES AND PROFITS</span></h1>
  <div class="abs title-rule"></div>
  <div class="abs brand"><span class="dot"></span>KWRO</div>

  <p class="abs body-text ragged" style="left:34px;top:114px;width:142px">KWRO’s process is shown in Figure 5 below. The shipper uses the TMS to obtain quotes and book and track their freight. The data captured in the TMS is downloaded and processed by KWRO. Easy to read “dashboard” reports are provided to management with more comprehensive reports available as required. The results are reviewed monthly with management and recommendations for improvements in the logistics system are presented.</p>

  <div class="abs caption" style="left:34px;top:302px;width:136px;height:74px">
    <span class="fig">FIGURE 6.</span>
    <span class="note" style="margin-top:8px">Using a TMS to quote, book and capture data then having KWRO filter and analyze the data pays dividends in process improvement and lower costs.</span>
  </div>

  <div class="abs diagram">
    <svg width="322" height="272" viewBox="0 0 322 272" font-family="Arimo, Arial, sans-serif">
      <defs>
        <g id="token"><circle r="12" fill="var(--token)"/><text y="5" text-anchor="middle" font-size="14" font-weight="700" fill="#fff">T</text></g>
      </defs>
      <text x="216" y="14" font-size="9.5" font-weight="700" fill="#222">Queries /Booking</text>
      <use href="#token" x="186" y="34"/>
      <circle cx="227" cy="34" r="12" fill="var(--red)"/><text x="227" y="39" text-anchor="middle" font-size="14" font-weight="700" fill="#fff">T</text>
      <use href="#token" x="279" y="34"/>
      <g fill="none" stroke="var(--red)" stroke-width="1.8">
        <path d="M183 60l3-3 3 3M183 66l3 3 3-3"/>
        <path d="M224 60l3-3 3 3M224 66l3 3 3-3"/>
        <path d="M262 62l0-3 3 0M270 68l3 0 0-3"/>
      </g>
      <rect x="14" y="77" width="90" height="117" fill="#fff" stroke="var(--red)" stroke-width="1.2"/>
      <rect x="20" y="184" width="78" height="4" fill="var(--red)"/>
      <text x="20" y="143" font-size="14" font-weight="700" fill="var(--red)">SHIPPER</text>
      <rect x="153" y="77" width="89" height="117" fill="#fff" stroke="var(--red)" stroke-width="1.2"/>
      <rect x="159" y="184" width="77" height="4" fill="var(--red)"/>
      <text x="160" y="143" font-size="14" font-weight="700" fill="var(--red)">TMS</text>
      <text x="128" y="96" text-anchor="middle" font-size="8" font-weight="700" fill="#222">Quotes</text>
      <text x="128" y="106" text-anchor="middle" font-size="8" font-weight="700" fill="#222">/Booking</text>
      <text x="130" y="176" text-anchor="middle" font-size="8" font-weight="700" fill="#222">Historical</text>
      <text x="130" y="186" text-anchor="middle" font-size="8" font-weight="700" fill="#222">Data</text>
      <g fill="none" stroke="var(--red)" stroke-width="2">
        <path d="M117 134l-4 4 4 4M138 134l4 4-4 4"/>
        <path d="M256 90l-3 4 3 4M264 90l3 4-3 4"/>
        <path d="M256 137l-3 4 3 4M264 137l3 4-3 4"/>
        <path d="M256 185l-3 4 3 4M264 185l3 4-3 4"/>
      </g>
      <use href="#token" x="289" y="94"/>
      <use href="#token" x="289" y="141"/>
      <use href="#token" x="289" y="189"/>
      <g fill="none" stroke="var(--red)" stroke-width="1.8">
        <path d="M92 202l3-3 3 3M92 208l3 3 3-3"/>
        <path d="M155 202l3-3 3 3M155 208l3 3 3-3"/>
        <path d="M183 214l3-3 3 3M183 220l3 3 3-3"/>
        <path d="M224 214l3-3 3 3M224 220l3 3 3-3"/>
        <path d="M262 215l0-3 3 0M270 221l3 0 0-3"/>
      </g>
      <rect x="90" y="215" width="76" height="43" fill="#fff" stroke="var(--red)" stroke-width="1.2"/>
      <rect x="96" y="250" width="64" height="3" fill="var(--red)"/>
      <text x="128" y="240" text-anchor="middle" font-size="13" font-weight="700" fill="var(--red)">TMS</text>
      <use href="#token" x="186" y="246"/>
      <use href="#token" x="227" y="246"/>
      <use href="#token" x="279" y="246"/>
    </svg>
  </div>

  <p class="abs body-text" style="left:34px;top:398px;width:440px">Bottom line, simplify your freight booking processes and reduce pricing by using a TMS provided by a 3PL. Capture the knowledge that your historical data contains, analyze it and take actions that will improve your processes and your profit.</p>
  <div class="abs footer-rule" style="left:34px;top:438px;width:440px"></div>

  <h2 class="abs section-head" style="left:34px;top:458px">KWRO is There When You Need Help or Advice</h2>
  <p class="abs body-text" style="left:34px;top:486px;width:440px">At the beginning of this paper, “value” was mentioned as being beyond just the price to include reliability, ease of use, availability of help when needed and so forth. In addition to bringing added value by helping you benefit from the data you are generating with each shipment, KWRO is able to work with you when you need to switch modes or evaluate a new distribution plan. If you typically ship LTL but suddenly have a need for an expedited air shipment for an important order, KWRO can help you move that without having to start from scratch. KWRO’s 3PL partners will provide the same reliable service and significant buying power whether you ship by air, ocean, truck or intermodal. International and domestic services are also easily handled.</p>
  <p class="abs body-text" style="left:34px;top:590px;width:440px">If you’d like to know more, contact the author, Dana Morrow, at dana@kwrofreight.example and start harnessing your data to improve profits.</p>

  <div class="abs footer-rule" style="left:34px;top:644px;width:400px"></div>
  <span class="abs page-num" style="left:466px;top:640px">06</span>
</section>

</body>
</html>
```